Web Page Re-designed

Looking to have this portion of a webpage on my site re-designed to look a little more clean and professional, the layout and organization of the data can be changed for example the location name does not have to keep repeating itself its schedule for a sports league

Reason: Still looking fo the right design

```html
<!DOCTYPE html>
<html lang="en">
<head>
<meta charset="utf-8">
<title>Kestrel Sports – Wednesday Co-Ed Ball Hockey Schedule</title>
<link href="https://fonts.googleapis.com/css2?family=Arimo:ital,wght@0,400;0,700;1,400;1,700&display=swap" rel="stylesheet">
<style>
  :root{
    --page-green:#7bb33c;
    --page-green-light:#9ccb5e;
    --brand-green:#76b041;
    --tab-yellow:#fbe77a;
    --panel:#f7f7f2;
    --ink:#333;
    --ink-soft:#555;
    --black:#111;
    --venue-red:#d0231c;
    --vs-yellow:#fcd92f;
    --row-alt:#f2f2f2;
    --line:#dcdcdc;
    --white:#fff;
  }
  *{box-sizing:border-box;margin:0;padding:0}
  html,body{width:1200px;height:1000px;overflow:hidden}
  body{
    position:relative;
    font-family:"Arimo",Arial,sans-serif;
    color:var(--ink);
    background:radial-gradient(ellipse 900px 600px at 600px 120px,var(--page-green-light),var(--page-green) 70%);
  }
  a{color:inherit}

  .utility-nav{position:absolute;left:579px;top:2px;width:530px;height:23px;display:flex;background:var(--tab-yellow);border:1px solid #d9b93a;border-top:0;border-radius:0 0 3px 3px}
  .utility-nav a{flex:auto;text-align:center;font-size:15px;line-height:21px;text-decoration:none;color:#1a3a10;border-right:1px solid #b59a2a}
  .utility-nav a:last-child{border-right:0}

  .brand{position:absolute;left:112px;top:28px;font-size:38px;font-weight:700;color:var(--white);letter-spacing:-1px}

  .main-nav{position:absolute;left:516px;top:42px;width:593px;height:50px;background:var(--black);border-radius:6px 2px 8px 3px;display:flex;align-items:center;justify-content:flex-end;padding-right:10px}
  .main-nav a{color:var(--white);font-style:italic;font-size:16px;text-decoration:underline;padding:0 12px;border-left:1px solid #555}
  .main-nav a:first-child{border-left:0}

  .panel{position:absolute;left:109px;top:107px;width:1000px;height:804px;background:var(--panel);border-radius:8px;box-shadow:0 2px 6px rgba(0,0,0,.3)}

  .hero{position:absolute;left:125px;top:121px;width:968px;height:114px;border-radius:4px;background:linear-gradient(90deg,#cfd6c4 0%,#b4bf9f 35%,#6aa02e 70%,#4c8a1f 100%)}
  .social-badge{position:absolute;left:867px;top:145px;width:175px;height:66px;background:var(--black);border-radius:6px;display:flex;align-items:center;gap:12px;padding-left:14px}
  .social-badge .mark{width:38px;height:38px;background:#4a6aa8;border-radius:5px}
  .social-badge span{color:var(--white);font-style:italic;font-size:17px;line-height:17px}

  .title-bar{position:absolute;left:126px;top:249px;width:967px;height:27px;background:#333;border-radius:3px 3px 0 0;color:var(--white);font-weight:700;font-style:italic}
  .title-bar h1{position:absolute;left:35px;top:6px;font-size:10px;text-transform:uppercase}
  .season{position:absolute;left:790px;top:5px;font-size:13px;display:flex;gap:6px;align-items:center}
  .season .select{width:106px;height:17px;background:var(--white);color:var(--ink);border:1px solid #888;font-size:12px;font-style:normal;font-weight:400;padding-left:4px;line-height:15px;position:relative}
  .season .select::after{content:"";position:absolute;right:1px;top:1px;width:13px;height:13px;background:#ddd;border:1px solid #555}

  .side-box{position:absolute;left:126px;width:194px;background:var(--white);border-radius:6px;border:1px solid #ececec}
  .side-box h2{background:var(--brand-green);color:var(--white);font-size:14px;font-style:italic;text-align:center;height:25px;line-height:25px;border-radius:5px 5px 0 0}
  .side-box ul{list-style:none;padding:2px 0 0 10px}
  .side-box li{font-size:13px;font-weight:700;font-style:italic;color:var(--black);line-height:24px}
  .side-box li::before{content:"•";margin-right:8px}

  .team-select{position:absolute;left:342px;top:291px;width:259px;height:44px;background:var(--brand-green);color:var(--white);font-size:15px;line-height:44px;padding-left:18px;border-radius:2px}
  .type-select{position:absolute;left:834px;top:291px;width:259px;height:44px;background:#ebebeb;color:var(--black);font-size:14px;line-height:44px;padding-left:20px;border-radius:2px}
  .team-select::after,.type-select::after{content:"";position:absolute;right:0;top:0;width:33px;height:44px;border-left:1px solid rgba(0,0,0,.2)}
  .caret{position:absolute;right:8px;top:16px;width:0;height:0;border-left:9px solid transparent;border-right:9px solid transparent;border-top:15px solid #2f5a12}
  .type-select .caret{border-top-color:#888}

  .day{position:absolute;left:342px;width:751px}
  .day h3{height:36px;line-height:36px;text-align:center;color:var(--white);font-size:17px;background:linear-gradient(#444,#000);border-radius:3px;margin-bottom:7px}
  .games{width:100%;border-collapse:collapse;table-layout:fixed;font-size:14px}
  .games th{background:var(--brand-green);color:var(--white);font-size:14px;text-align:left;height:33px;padding-left:14px}
  .games th.time{text-align:center;padding-left:0}
  .games td{height:45px;border:1px solid var(--line);padding:0 6px;background:var(--white)}
  .games tr.alt td{background:var(--row-alt)}
  .games td.location{height:36px;background:#f1f1f1;font-weight:700;color:var(--ink-soft);border-left:0;border-right:0;padding-left:5px}
  .games td.location b{color:var(--venue-red)}
  .games td.shirt{text-align:center}
  .games td.vs{background:var(--vs-yellow)!important;text-align:center;font-size:17px;border-color:var(--vs-yellow)}
  .games td.team{padding-left:11px}
  .games td.sticks{padding-left:10px}
  .jersey{width:22px;height:21px;vertical-align:middle}
</style>
</head>
<body>
<svg width="0" height="0" style="position:absolute">
  <defs>
    <symbol id="jersey" viewBox="0 0 26 24">
      <path d="M8 1 L2 4 L0 10 L5 11 L5 23 L21 23 L21 11 L26 10 L24 4 L18 1 Q13 5 8 1 Z" stroke="#555" stroke-width="1"/>
    </symbol>
  </defs>
</svg>

<nav class="utility-nav">
  <a href="#">Home</a><a href="#">About Us</a><a href="#">FAQS</a><a href="#">Contact Us</a><a href="#">Jobs</a><a href="#">Sponsors</a>
</nav>
<div class="brand">Kestrel Sports</div>
<nav class="main-nav">
  <a href="#">Leagues</a><a href="#">Schedules &amp; More</a><a href="#">Register</a><a href="#">Pay</a><a href="#">Forum</a><a href="#">Tournaments</a>
</nav>

<div class="panel"></div>
<div class="hero" role="img" aria-label="Banner photo of league players in hockey jerseys"></div>
<div class="social-badge"><div class="mark"></div><span>Find Us On<br>Huddle</span></div>

<div class="title-bar">
  <h1>Wednesday Co-Ed Ball Hockey Schedule</h1>
  <div class="season">Season: <div class="select">Fall 2013</div></div>
</div>

<aside class="side-box" style="top:291px;height:130px">
  <h2>Schedules</h2>
  <ul><li>Division A</li><li>Division B</li><li>Division C</li></ul>
</aside>
<aside class="side-box" style="top:436px;height:178px">
  <h2>Quick Links</h2>
  <ul><li>Rules</li><li>Teams</li><li>News</li><li>Free Agents</li><li>Champ T-Shirt Request</li></ul>
</aside>
<aside class="side-box" style="top:629px;height:154px">
  <h2>Stats Menu</h2>
  <ul><li>Game Results</li><li>Scoreboard</li><li>Standings</li><li>Leaders</li></ul>
</aside>

<div class="team-select">-Select Team-<span class="caret"></span></div>
<div class="type-select">Regular Season/Exhibition<span class="caret"></span></div>

<section class="day" style="top:357px">
  <h3>Wed, Oct 2nd</h3>
  <table class="games">
    <colgroup><col style="width:31px"><col style="width:71px"><col style="width:58px"><col style="width:180px"><col style="width:55px"><col style="width:56px"><col style="width:221px"><col style="width:79px"></colgroup>
    <tr><th colspan="2" class="time">Time</th><th colspan="3">Home</th><th colspan="2" style="padding-left:11px">Away</th><th>Sticks</th></tr>
    <tr><td colspan="8" class="location">Location : <b>Maple Ridge Centre</b></td></tr>
    <tr><td>RS</td><td>8:00 pm</td><td class="shirt"><svg class="jersey" fill="#f7941d"><use href="#jersey"/></svg></td><td class="team">RIPTIDE</td><td class="vs">Vs.</td><td class="shirt"><svg class="jersey" fill="#fff200"><use href="#jersey"/></svg></td><td class="team">Tape To Tape</td><td class="sticks"></td></tr>
    <tr class="alt"><td>RS</td><td>9:00 pm</td><td class="shirt"><svg class="jersey" fill="#fff"><use href="#jersey"/></svg></td><td class="team">Cold Front Flyers</td><td class="vs">Vs.</td><td class="shirt"><svg class="jersey" fill="#000"><use href="#jersey"/></svg></td><td class="team">Puckmasters</td><td class="sticks"></td></tr>
  </table>
</section>

<section class="day" style="top:574px">
  <h3>Wed, Oct 9th</h3>
  <table class="games">
    <colgroup><col style="width:31px"><col style="width:71px"><col style="width:58px"><col style="width:180px"><col style="width:55px"><col style="width:56px"><col style="width:221px"><col style="width:79px"></colgroup>
    <tr><th colspan="2" class="time">Time</th><th colspan="3">Home</th><th colspan="2" style="padding-left:11px">Away</th><th>Sticks</th></tr>
    <tr><td colspan="8" class="location">Location : <b>Maple Ridge Centre</b></td></tr>
    <tr><td>RS</td><td>7:00 pm</td><td class="shirt"><svg class="jersey" fill="#fff200"><use href="#jersey"/></svg></td><td class="team">Tape To Tape</td><td class="vs">Vs.</td><td class="shirt"><svg class="jersey" fill="#8e5aa8"><use href="#jersey"/></svg></td><td class="team">Odd Socks</td><td class="sticks"></td></tr>
    <tr><td colspan="8" class="location">Location : <b>Eastbrook (EBK)</b></td></tr>
    <tr><td>RS</td><td>8:45 pm</td><td class="shirt"><svg class="jersey" fill="#000"><use href="#jersey"/></svg></td><td class="team">Puckmasters</td><td class="vs">Vs.</td><td class="shirt"><svg class="jersey" fill="#fff"><use href="#jersey"/></svg></td><td class="team">Them Folks</td><td class="sticks">No Wood</td></tr>
    <tr class="alt"><td>RS</td><td>9:45 pm</td><td class="shirt"><svg class="jersey" fill="#fff"><use href="#jersey"/></svg></td><td class="team">Cold Front Flyers</td><td class="vs">Vs.</td><td class="shirt"><svg class="jersey" fill="#f7941d"><use href="#jersey"/></svg></td><td class="team">RIPTIDE</td><td class="sticks">No Wood</td></tr>
  </table>
</section>
</body>
</html>
```